Aisle signage for supermarket

Design Isle signs for Indian supermarket. Modern, Clear, legible. Would be nice to use our logo colours. Signs Will be double sided and measure 900mm width x 400mm height. Indian theme would be nice. Attached files shows description to go on each sign.
Font styles to use
Sans Serif
Colors
Designer to choose colors to be used in the design.

```html
<!DOCTYPE html>
<html lang="en">
<head>
<meta charset="utf-8">
<title>Aisle 2 – Dry Fruits, Nuts, Lentils / Dall</title>
<link rel="stylesheet" href="https://fonts.googleapis.com/css2?family=Oswald:wght@500;700&display=swap">
<style>
  :root {
    --green-deep: #006a3b;
    --green-pattern: #0f7244;
    --green-lime: #8dc63f;
    --green-mid: #3f9a3e;
    --white: #ffffff;
    --ink-green: #0b6b3a;
  }
  html, body {
    margin: 0;
    padding: 0;
    width: 1200px;
    height: 800px;
    overflow: hidden;
    background: var(--white);
  }
  .aisle-sign {
    position: relative;
    width: 1200px;
    height: 800px;
    overflow: hidden;
    font-family: "Oswald", "Arial Narrow", sans-serif;
  }
  .sign-header {
    position: absolute;
    left: 0; top: 0;
    width: 1200px; height: 153px;
    background: linear-gradient(to bottom,
      var(--ink-green) 0%,
      #9fc9ad 22%,
      var(--white) 52%,
      #e2f1cf 72%,
      var(--green-lime) 100%);
    display: flex;
    align-items: center;
    justify-content: center;
  }
  .brand-name {
    margin: 0;
    font-weight: 500;
    font-size: 62px;
    letter-spacing: 10px;
    color: var(--ink-green);
    line-height: 1;
  }
  .sign-field {
    position: absolute;
    left: 0; top: 153px;
    width: 1200px; height: 647px;
    background:
      radial-gradient(circle at 30% 40%, var(--green-pattern) 0%, transparent 45%),
      radial-gradient(circle at 75% 70%, var(--green-pattern) 0%, transparent 40%),
      var(--green-deep);
  }
  .sign-content {
    position: absolute;
    left: 0; top: 0;
    width: 1200px; height: 800px;
  }
  .category-text {
    font-family: "Oswald", "Arial Narrow", sans-serif;
    font-weight: 700;
    fill: var(--white);
  }
  .pointer { fill: var(--green-lime); }
</style>
</head>
<body>
<main class="aisle-sign">
  <header class="sign-header">
    <h1 class="brand-name">TARAN BROTHERS</h1>
  </header>

  <div class="sign-field" role="img" aria-label="Faint Indian floral paisley pattern on deep green"></div>

  <svg class="sign-content" width="1200" height="800" viewBox="0 0 1200 800">
    <defs>
      <linearGradient id="divider-fade" x1="0" y1="0" x2="1" y2="0">
        <stop offset="0.04" stop-color="#ffffff"/>
        <stop offset="0.5" stop-color="#8dc63f"/>
        <stop offset="0.72" stop-color="#6fb23c"/>
        <stop offset="1" stop-color="#006a3b"/>
      </linearGradient>
    </defs>

    <rect class="section-divider" x="0" y="567" width="1200" height="31" fill="url(#divider-fade)"/>
    <rect class="section-divider" x="0" y="770" width="1200" height="30" fill="url(#divider-fade)"/>

    <polygon class="pointer" points="0,232 58,284 0,335"/>
    <polygon class="pointer" points="0,648 58,700 0,752"/>

    <text class="category-text" x="84" y="343" font-size="148" textLength="610" lengthAdjust="spacingAndGlyphs">DRY FRUITS</text>
    <text class="category-text" x="84" y="497" font-size="148" textLength="270" lengthAdjust="spacingAndGlyphs">NUTS</text>
    <text class="category-text" x="84" y="750" font-size="148" textLength="811" lengthAdjust="spacingAndGlyphs">LENTILS&#160;&#160;/&#160;DALL</text>

    <text class="category-text aisle-number" x="1004" y="828" font-size="820" textLength="212" lengthAdjust="spacingAndGlyphs">2</text>
  </svg>
</main>
</body>
</html>
```